Postcard About Outsourcing Paperwork

Pemberton, Inc. help nonprofits register so that they can solicit contributions in various states so essentially we are a consulting company who handles paperwork for charities. I have uploaded our logo and a couple other images that we have on our website. We want an oversized post card which on the front says something like "Tired of signing your state registrations". On the back of the card, the right half the card will need name for addresses to print. the right will have spiel about us, but could also have images. The verbiage will be something like "Not only can we file your state registrations, but we can sign and notarize them, and can cut the checks for the state fees. Pemberton file tens of thousands of state registrations each year. Call us today at 760-555-0147 or email us at info@pembertoninc.example to see how we can help you. You can also visit our website at www.pembertoninc.example"

Target Market(s)

We are targeting Charities

Industry/Entity Type

It Company

Requirements
Nice to have
• Our logo(uploaded) and the color blue (matching our logo, website, letterhead) could be good to have

```html
<!DOCTYPE html>
<html lang="en">
<head>
<meta charset="utf-8">
<title>Pemberton, Inc. – Postcard Back</title>
<link rel="stylesheet" href="https://fonts.googleapis.com/css2?family=Source+Sans+3:wght@400;600&display=swap">
<style>
  :root {
    --paper: #ffffff;
    --frame-blue: #1ba1e2;
    --link-blue: #1a7fc1;
    --ink: #1e1e1e;
    --rule: #6b6b6b;
    --box-line: #222222;
    --brand-blue: #2a5f9e;
  }
  html, body {
    margin: 0;
    padding: 0;
    overflow: hidden;
    background: var(--paper);
  }
  .postcard {
    position: relative;
    width: 1200px;
    height: 779px;
    box-sizing: border-box;
    border: 7px solid var(--frame-blue);
    background: var(--paper);
    font-family: "Source Sans 3", Arial, sans-serif;
    color: var(--ink);
    overflow: hidden;
  }
  .pitch {
    position: absolute;
    left: 0;
    top: 58px;
    width: 1030px;
    margin: 0;
    text-align: center;
    font-size: 28px;
    line-height: 37.5px;
  }
  .pitch p { margin: 0; }
  .pitch .accent { color: var(--link-blue); }
  .postage-area {
    position: absolute;
    left: 995px;
    top: 12px;
    width: 172px;
    height: 178px;
    border: 2px solid var(--box-line);
    box-sizing: border-box;
    text-align: center;
    font-size: 18px;
    line-height: 24px;
    padding-top: 50px;
  }
  .brand {
    position: absolute;
    left: 888px;
    top: 208px;
    display: flex;
    align-items: center;
    gap: 12px;
  }
  .brand-square {
    width: 64px;
    height: 64px;
    background: var(--brand-blue);
  }
  .brand-name {
    font-size: 30px;
    font-weight: 600;
    color: var(--brand-blue);
  }
  .mailing-panel {
    position: absolute;
    left: 20px;
    top: 333px;
    width: 1142px;
    height: 409px;
    border: 2px solid var(--box-line);
    box-sizing: border-box;
  }
  .recipient-title {
    position: absolute;
    left: 250px;
    top: 38px;
    margin: 0;
    font-size: 27px;
    font-weight: 400;
  }
  .field {
    position: absolute;
    left: 14px;
    display: flex;
    align-items: flex-end;
    font-size: 27px;
    line-height: 30px;
  }
  .field-label { display: inline-block; }
  .field-line {
    position: absolute;
    left: 116px;
    width: 394px;
    bottom: 6px;
    border-bottom: 4px solid var(--rule);
  }
  .field.name { top: 118px; }
  .field.state { top: 216px; }
  .field.city { top: 252px; }
  .field.street { top: 288px; }
  .address-column {
    position: absolute;
    left: 772px;
    top: 0;
    width: 366px;
    height: 405px;
    border-left: 2px solid var(--box-line);
  }
  .address-area {
    position: absolute;
    left: 0;
    top: 0;
    width: 100%;
    height: 326px;
    border-bottom: 2px solid var(--box-line);
    text-align: center;
    font-size: 19px;
    line-height: 26px;
    box-sizing: border-box;
    padding-top: 128px;
  }
  .barcode-area {
    position: absolute;
    left: 10px;
    top: 357px;
    font-size: 19px;
  }
</style>
</head>
<body>
  <main class="postcard">
    <section class="pitch">
      <p>Not only can we file your state registrations,</p>
      <p>but we can sign and notarize them, and can cut the checks for the state fees.</p>
      <p>Pemberton file tens of thousands of state registrations each year.</p>
      <p><span class="accent">Call</span> us today at <span class="accent">760-555-0147</span></p>
      <p>or email us at <span class="accent">info@pembertoninc.example</span></p>
      <p>to see how we can help you.</p>
      <p>You can also visit our website at <span class="accent">www.pembertoninc.example</span></p>
    </section>

    <div class="postage-area">Postage<br>Area</div>

    <div class="brand">
      <span class="brand-square"></span>
      <span class="brand-name">Pemberton, Inc.</span>
    </div>

    <section class="mailing-panel">
      <h2 class="recipient-title">RECIPIENT ADDRESS:</h2>
      <div class="field name"><span class="field-label">NAME:</span><span class="field-line"></span></div>
      <div class="field state"><span class="field-label">STATE:</span><span class="field-line"></span></div>
      <div class="field city"><span class="field-label">&nbsp;&nbsp;CITY:</span><span class="field-line"></span></div>
      <div class="field street"><span class="field-label">STREET:</span><span class="field-line"></span></div>

      <div class="address-column">
        <div class="address-area">Address<br>Area</div>
        <div class="barcode-area">Barcode Area</div>
      </div>
    </section>
  </main>
</body>
</html>
```